we can communicate on this, but i want to follow the approach we took on Pell|Quorn & Tillet but i feel the card front needs the black background and the platinum and gold logo. The back? I am open. we can use the same info from PQ&T. Vellum Crest is an enhanced equity investment fund - basically a very exclusive boutique hedge fund that uses only stock options. very advanced things. hope you are interested

Contact Information for Business Card

Dr. Owen T. Brisket, CFA
Scientifique de fusée financière
555.014.2296
TheDoc4793@mailvessel.example

4718 Fennel Brook Way N.
West Fargo, ND 58078

No web site

Colors

Designer to choose colors to be used in the design.

Requirements
Nice to have
• I tend to prefer the most visible applications of the logo to include logo and name, the logo version with a black background and the gold and platinum components separated by the black. I see this working well for a single side (logo and name - this is card front to me).
• I am fairly open to other treatments on the reverse side with the data. To me, it makes sense to have a different color rendition of the logo on the reverse and it may be a muted black tone on tone or an oversized portion that would have spot UV. Or, the reverse may play with colors and layout
Should not have
• Other colors = no no
• Decorative font

```html
<!DOCTYPE html>
<html lang="en">
<head>
<meta charset="utf-8">
<title>Vellum Crest – Business Card</title>
<link href="https://fonts.googleapis.com/css2?family=Montserrat:wght@600&family=Roboto:wght@400;700&display=swap" rel="stylesheet">
<style>
  :root {
    --backdrop: #3b3b3d;
    --card: #1b1b1d;
    --tone-on-tone: #2a2a2d;
    --gold: #d4a62a;
    --platinum: #f2f2f2;
    --muted: #cfcfcf;
  }
  * { margin: 0; padding: 0; box-sizing: border-box; }
  html, body { width: 799px; height: 1200px; overflow: hidden; }
  body {
    background: var(--backdrop);
    position: relative;
    font-family: "Roboto", Arial, sans-serif;
  }
  .card {
    position: absolute;
    left: 80px;
    width: 640px;
    height: 366px;
    background: var(--card);
    border-radius: 3px;
    box-shadow: 0 10px 28px rgba(0,0,0,.45);
    overflow: hidden;
  }
  .card--front { top: 135px; }
  .card--back { top: 700px; }

  /* Front: gold and platinum brand block */
  .front-brand {
    position: absolute;
    left: 0; right: 0; top: 78px;
    display: flex;
    flex-direction: column;
    align-items: center;
    gap: 18px;
  }
  .front-brand .mark-circle {
    width: 120px; height: 120px;
    border-radius: 50%;
    background: var(--gold);
  }
  .front-brand .brand-name {
    font-family: "Montserrat", Arial, sans-serif;
    font-weight: 600;
    font-size: 46px;
    letter-spacing: 1px;
    text-transform: uppercase;
    color: var(--platinum);
  }

  /* Back: tone-on-tone brand block */
  .back-brand {
    position: absolute;
    left: 30px; top: 100px;
    width: 280px;
    display: flex;
    flex-direction: column;
    align-items: center;
    gap: 14px;
  }
  .back-brand .mark-circle {
    width: 86px; height: 86px;
    border-radius: 50%;
    background: var(--tone-on-tone);
  }
  .back-brand .brand-name {
    font-family: "Montserrat", Arial, sans-serif;
    font-weight: 600;
    font-size: 30px;
    letter-spacing: .5px;
    text-transform: uppercase;
    color: var(--platinum);
    white-space: nowrap;
  }

  /* Back: contact details */
  .contact {
    position: absolute;
    left: 340px; top: 108px;
    width: 280px;
    color: var(--platinum);
    font-size: 15px;
    line-height: 1.45;
  }
  .contact .person-name {
    color: var(--gold);
    font-weight: 700;
    font-size: 19px;
    white-space: nowrap;
  }
  .contact .person-role { font-size: 14px; color: var(--muted); margin-bottom: 16px; white-space: nowrap; }
  .contact-row { display: flex; align-items: center; gap: 10px; white-space: nowrap; }
  .contact-row svg { width: 13px; height: 13px; flex: none; fill: var(--gold); }
  .contact .address { margin-top: 6px; }
</style>
</head>
<body>

  <section class="card card--front" aria-label="Card front">
    <div class="front-brand">
      <div class="mark-circle"></div>
      <div class="brand-name">Vellum Crest</div>
    </div>
  </section>

  <section class="card card--back" aria-label="Card back">
    <div class="back-brand">
      <div class="mark-circle"></div>
      <div class="brand-name">Vellum Crest</div>
    </div>

    <div class="contact">
      <div class="person-name">Dr. Owen T. Brisket, CFA</div>
      <div class="person-role">Scientifique de fusée financière</div>

      <div class="contact-row">
        <svg viewBox="0 0 16 16" aria-hidden="true"><path d="M3 1h3l1.5 4-2 1.2a9 9 0 0 0 4.3 4.3L11 8.5l4 1.5v3a2 2 0 0 1-2 2A12 12 0 0 1 1 3a2 2 0 0 1 2-2z"/></svg>
        <span>555.014.2296</span>
      </div>
      <div class="contact-row">
        <svg viewBox="0 0 16 16" aria-hidden="true"><path d="M1 3h14v10H1z M1 3l7 6 7-6" stroke="#1b1b1d" stroke-width="1.2"/></svg>
        <span>TheDoc4793@mailvessel.example</span>
      </div>
      <div class="address">4718 Fennel Brook Way N.<br>West Fargo, ND 58078</div>
    </div>
  </section>

</body>
</html>
```